Anzeigengestaltung für Stellenausschreibung
Zielgruppe
Seit mehr als 15 Jahren verkaufen wir weltweit neue und generalüberholte Netzwerktechnik und haben uns zu einer starken Marke in der Branche entwickelt. Tagtäglich arbeitet unser einzigartiges Team mit vollem Einsatz daran, dass wir auf unserem Gebiet immer besser werden - und unsere Kunden auch weiterhin mit überzeugenden Angeboten für uns gewinnen können. Ob Vertrieb oder Lager, ob Marketing oder Buchhaltung: Wir geben immer unser Bestes, um die Zukunft von Nordwerkhandel zu gestalten. Denn „Let’s live IT“ ist nicht nur unser Slogan, sondern beschreibt unsere Leidenschaft.
Aufgabenstellung
Wir brauchen eine aussagekräftige Stellenausschreibung (im DIN A4 Format) für unsere Sales (Vertrieb) Stelle. Uns fehlt es an guten Bewerbungen besonders für diese Stelle. Die Verdienstmöglichkeiten sind super, nur man muss halt Bock haben auf Verkaufen. Das coole ist, man muss die Kunden nicht anrufen oder Kalt-Akquise betreiben, sondern der Kunde kommt, über unseren Shop, auf uns zu mit einer Anfrage.
Ein treffender Slogan wäre mega uns fällt da nix richtiges ein aber Aussagen wie:
• Sag uns was du kannst wir haben sicher dich richtige Stelle für dich
• Du hast bock auf richtig fette Kohle
• Sag uns was du verdienen möchtest wir machen es für dich möglich
• Kein Klinken putzen keine Kaltakquise bei uns kommen die Kunden auf dich zu
Gerne soll es witzig sein (auf Flachwitze), frech, provokant - eben etwas was man nicht alle Tage sieht .
Die Zielgruppe soll die 'breite Masse' sein.

```html
<!DOCTYPE html>
<html lang="de">
<head>
<meta charset="utf-8">
<title>Stellenanzeige Vertrieb – Nordwerkhandel</title>
<link rel="stylesheet" href="https://fonts.googleapis.com/css2?family=League+Spartan:wght@400;700;800&family=Yellowtail&family=Pacifico&family=Poppins:wght@400&display=swap">
<style>
  :root {
    --orange: #f37f2a;
    --orange-shade: #e2622a;
    --orange-tint: #fbd9bf;
    --ink: #3d3d3f;
    --paper: #ffffff;
    --backdrop: #9c9c9c;
  }
  html, body {
    margin: 0;
    width: 1200px;
    height: 1177px;
    overflow: hidden;
    background: var(--backdrop);
  }
  .poster {
    position: absolute;
    left: 159px;
    top: 18px;
    width: 882px;
    height: 1140px;
    display: block;
  }
  .headline { font-family: "League Spartan", "Montserrat", sans-serif; font-weight: 800; }
  .headline--big { font-size: 250px; }
  .headline--line { font-size: 88px; }
  .headline--kommen { font-size: 240px; fill: var(--ink); }
  .white { fill: var(--paper); }
  .shade { fill: var(--orange-shade); }
  .script { font-family: "Yellowtail", "Pacifico", cursive; font-size: 170px; fill: var(--orange); }
  .body-copy { font-family: "Poppins", sans-serif; font-size: 17px; fill: var(--ink); }
  .hashtag { font-family: "League Spartan", sans-serif; font-weight: 700; font-size: 31px; fill: var(--orange); }
  .brand-name { font-family: "League Spartan", sans-serif; font-weight: 700; font-size: 44px; fill: var(--orange); }
</style>
</head>
<body>
<svg class="poster" viewBox="0 0 1288 1665" xmlns="http://www.w3.org/2000/svg" aria-label="Stellenanzeige: Kein Klinken putzen, keine Kaltakquise – bei uns kommen die Kunden auf dich zu">
  <defs>
    <radialGradient id="idea-glow" cx="50%" cy="45%" r="60%">
      <stop offset="0" stop-color="var(--orange-tint)"/>
      <stop offset="1" stop-color="var(--paper)"/>
    </radialGradient>
  </defs>
  <rect width="1288" height="1665" fill="var(--paper)"/>

  <g class="slogan" transform="translate(102 270) rotate(-15)">
    <polyline points="-420,-48 743,-48 745,192 1200,194" fill="none" stroke="var(--orange)" stroke-width="3"/>
    <line x1="-340" y1="776" x2="74" y2="776" stroke="var(--orange)" stroke-width="3"/>

    <g fill="var(--orange)">
      <rect x="0" y="0" width="695" height="236"/>
      <rect x="-112" y="234" width="920" height="112"/>
      <rect x="0" y="344" width="696" height="234"/>
      <rect x="-200" y="575" width="1096" height="108"/>
      <rect x="74" y="722" width="548" height="104"/>
    </g>

    <text class="headline headline--big shade" x="70" y="224" textLength="560" lengthAdjust="spacingAndGlyphs">KEIN</text>
    <text class="headline headline--big white" x="60" y="218" textLength="560" lengthAdjust="spacingAndGlyphs">KEIN</text>
    <text class="headline headline--line white" x="-45" y="318" textLength="770" lengthAdjust="spacingAndGlyphs">KLINKEN PUTZEN</text>
    <text class="headline headline--big shade" x="50" y="554" textLength="600" lengthAdjust="spacingAndGlyphs">KEIN</text>
    <text class="headline headline--big white" x="40" y="548" textLength="600" lengthAdjust="spacingAndGlyphs">KEIN</text>
    <text class="headline headline--line white" x="-149" y="657" textLength="1004" lengthAdjust="spacingAndGlyphs">KALTAKQUISE BEI UNS</text>
    <text class="headline headline--line white" x="157" y="803" textLength="375" lengthAdjust="spacingAndGlyphs">KUNDEN</text>
    <text class="headline headline--kommen" x="-205" y="1023" textLength="1095" lengthAdjust="spacingAndGlyphs">KOMMEN</text>

    <line x1="-211" y1="1111" x2="-87" y2="1111" stroke="var(--orange)" stroke-width="10"/>
    <line x1="760" y1="1112" x2="885" y2="1112" stroke="var(--orange)" stroke-width="10"/>
    <text class="script" x="-60" y="1160" textLength="800" lengthAdjust="spacingAndGlyphs">Die auf dich zu</text>
  </g>

  <!-- idea symbol area -->
  <rect class="idea-area" x="896" y="400" width="180" height="200" rx="24" fill="url(#idea-glow)"
        transform="rotate(-15 986 500)" role="img" aria-label="Symbol einer leuchtenden Glühbirne als Zeichen für eine Idee"/>

  <g class="body-copy" text-anchor="end">
    <text x="1171" y="1366">Die Verdienstmöglichkeiten sind super, nur man</text>
    <text x="1171" y="1391">muss halt Bock haben auf Verkaufen. Das coole ist,</text>
    <text x="1171" y="1416">man muss die Kunden nicht anrufen oder</text>
    <text x="1171" y="1441">Kalt-Akquise betreiben, sondern der Kunde kommt,</text>
    <text x="1171" y="1466">über unseren Shop, auf uns zu mit einer Anfrage.</text>
  </g>

  <g class="social" fill="var(--orange)">
    <circle cx="442" cy="1515" r="24"/>
    <circle cx="513" cy="1515" r="24"/>
    <circle cx="583" cy="1515" r="24"/>
    <circle cx="654" cy="1515" r="24"/>
  </g>
  <text class="hashtag" x="124" y="1587" textLength="555" lengthAdjust="spacingAndGlyphs">#teamworkmakesthedreamwork</text>

  <circle cx="836" cy="1554" r="30" fill="var(--orange)"/>
  <text class="brand-name" x="878" y="1570" textLength="294" lengthAdjust="spacingAndGlyphs">Nordwerkhandel</text>

  <rect x="0" y="1647" width="644" height="18" fill="#262424"/>
  <rect x="644" y="1647" width="644" height="18" fill="var(--orange)"/>
</svg>
</body>
</html>
```